Lending Harbor Partners - business cards

we need new business cards for my company.
i've been in business for 25 years.
my wife and I are mortgage brokers.

we just bought the domain for a website with www.homekeyfunding.example
that could be used in the design also.

On the business card would be
Front card:

Dale Whitcomb
Owner/Loan Officer
Cell: (555) 314-2297
Lending Harbor Partners
4172 Pinecrest Lane
Brookhaven Springs, CA 95555
Office (555) 490-6631
Fax (555) 490-6674
website www.homekeyfunding.example

Back of Card:

LHP BRE #0378215 NMLS #586249
Dale Whitcomb BRE # 04519863 NMLS #587716

Industry/Entity Type

Business

```html
<!DOCTYPE html>
<html lang="en">
<head>
<meta charset="utf-8">
<title>Lending Harbor Partners – Business Cards</title>
<link href="https://fonts.googleapis.com/css2?family=Open+Sans:wght@300;400;600;700;800&display=swap" rel="stylesheet">
<style>
  :root {
    --backdrop: #8d8d8d;
    --card: #f7f7f5;
    --ink: #111111;
    --ink-soft: #2a2a2a;
    --muted: #6b6b6b;
    --brand-red: #d0102a;
  }
  * { box-sizing: border-box; margin: 0; padding: 0; }
  html, body {
    width: 1200px; height: 1000px; overflow: hidden;
    background: var(--backdrop);
    font-family: "Open Sans", Arial, sans-serif;
    color: var(--ink);
  }
  .sheet {
    width: 1200px; height: 1000px;
    display: flex; flex-direction: column;
    align-items: center; justify-content: center; gap: 40px;
  }
  .card {
    position: relative;
    width: 770px; height: 440px;
    background: var(--card);
    box-shadow: 0 6px 18px rgba(0,0,0,.25);
  }
  .brand { position: absolute; display: flex; align-items: center; }
  .brand-mark { background: var(--brand-red); flex: none; }
  .brand-name {
    font-weight: 800; text-transform: uppercase;
    color: var(--ink); line-height: .9; letter-spacing: -.5px;
  }
  /* front */
  .card-front .brand { left: 40px; top: 36px; gap: 18px; }
  .card-front .brand-mark { width: 140px; height: 140px; }
  .card-front .brand-name { font-size: 40px; }
  .person { position: absolute; right: 44px; top: 196px; text-align: right; }
  .person-name { font-size: 34px; font-weight: 700; line-height: 1.2; }
  .person-title { font-size: 26px; font-weight: 300; color: var(--ink-soft); }
  .contact {
    position: absolute; right: 44px; bottom: 30px; text-align: right;
    font-size: 20px; line-height: 1.5; color: var(--ink-soft);
  }
  .contact .label { font-weight: 700; color: var(--ink); }
  .contact .label-muted { font-weight: 700; color: var(--muted); }
  .contact .muted { color: var(--muted); }
  .divider { color: var(--brand-red); padding: 0 4px; }
  .website { color: var(--brand-red); font-weight: 700; font-size: 25px; }
  /* back */
  .card-back .brand { left: 40px; top: 36px; gap: 10px; }
  .card-back .brand-mark { width: 52px; height: 52px; }
  .card-back .brand-name { font-size: 16px; }
  .licenses {
    position: absolute; right: 44px; bottom: 40px; text-align: right;
    font-size: 20px; line-height: 1.45; letter-spacing: .3px; color: var(--ink-soft);
  }
</style>
</head>
<body>
<main class="sheet">
  <section class="card card-front" aria-label="Business card front">
    <div class="brand">
      <span class="brand-mark"></span>
      <span class="brand-name">Lending<br>Harbor<br>Partners</span>
    </div>
    <div class="person">
      <p class="person-name">Dale Whitcomb</p>
      <p class="person-title">Owner/Loan Officer</p>
    </div>
    <div class="contact">
      <p>4172 Pinecrest Lane, Brookhaven Springs, CA 95555</p>
      <p><span class="label-muted">Cell:</span> <span class="muted">(555) 314-2297</span><span class="divider">|</span><span class="label">Office</span> (555) 490-6631<span class="divider">|</span><span class="label">Fax</span> (555) 490-6674</p>
      <p class="website">www.homekeyfunding.example</p>
    </div>
  </section>

  <section class="card card-back" aria-label="Business card back">
    <div class="brand">
      <span class="brand-mark"></span>
      <span class="brand-name">Lending<br>Harbor<br>Partners</span>
    </div>
    <div class="licenses">
      <p>LHP BRE #0378215 NMLS #586249</p>
      <p>Dale Whitcomb BRE # 04519863 NMLS #587716</p>
    </div>
  </section>
</main>
</body>
</html>
```